Managed Service Provider need new business cards

We are a small Maanged Service Provider of IT Services and need a new fresh design for our business cards. We want something impossible, fun and professional :)
Our services has a large range, but we are always fun and make sure our customers both get their issue sorted and also feel like they are "catching up with an old friend".
All our cards in the past has always been all black, with red and we need something fresher.
The back of card, we would like just a small list of what we do i think, but if someone has a better idea, please do something cool with the back of the card:
Managed IT Services
Productivity Solutions
Data Backup and Recovery
IT System Maintenance
Managed IT Security
More details can be found on our website tqnetworks.com.au
Industry/Entity Type
It Company
Contact Information for Business Card
Name: Dwayne Falstrup
Title: Director
Phone: 03 6193 4827
Mobile: 0412 587 239
Email: dwayne@tqnetworks.com.au
Web: www.tqnetworks.com.au

```html
<!DOCTYPE html>
<html lang="en">
<head>
<meta charset="utf-8">
<title>TQ Networks – Business Card</title>
<link rel="stylesheet" href="https://fonts.googleapis.com/css2?family=Exo+2:wght@400;600;800&display=swap">
<style>
  :root {
    --stage: #2a2a2c;
    --card: #141414;
    --card-edge: #0b0b0b;
    --red: #e8202a;
    --white: #f2f2f2;
    --muted: #cfcfcf;
  }
  * { box-sizing: border-box; margin: 0; padding: 0; }
  html, body { width: 1200px; height: 900px; overflow: hidden; }
  body {
    background: var(--stage);
    font-family: "Exo 2", sans-serif;
    position: relative;
  }
  .card {
    position: absolute;
    left: 250px;
    width: 700px;
    height: 400px;
    background: linear-gradient(135deg, #1b1b1b 0%, var(--card) 55%, var(--card-edge) 100%);
    box-shadow: 0 14px 30px rgba(0,0,0,.55);
    overflow: hidden;
  }
  .card--front { top: 40px; }
  .card--back { top: 460px; }
  .card__lines { position: absolute; inset: 0; }

  .brand-name {
    position: absolute;
    color: var(--red);
    font-weight: 800;
    text-transform: uppercase;
    letter-spacing: 1px;
    line-height: 1;
  }
  .card--front .brand-name { left: 200px; top: 60px; font-size: 52px; }
  .card--back .brand-name { left: 455px; top: 300px; font-size: 34px; }

  .holder { position: absolute; left: 50px; top: 180px; }
  .holder__name {
    color: var(--red); font-weight: 800; font-size: 24px;
    text-transform: uppercase; letter-spacing: .5px;
  }
  .holder__title {
    color: var(--white); font-weight: 800; font-size: 17px;
    text-transform: uppercase; letter-spacing: 1px; margin-top: 2px;
  }

  .contacts {
    position: absolute; right: 40px; top: 290px;
    list-style: none; text-align: right;
  }
  .contacts li {
    display: flex; justify-content: flex-end; align-items: center; gap: 10px;
    color: var(--white); font-size: 15px; line-height: 22px; letter-spacing: .3px;
  }
  .contacts svg { width: 14px; height: 14px; flex: none; }

  .services { position: absolute; left: 38px; top: 52px; list-style: none; }
  .service {
    display: flex; align-items: center; gap: 16px;
    height: 56px;
    color: var(--white); font-size: 17px; font-weight: 600;
    text-transform: uppercase; letter-spacing: 1px;
  }
  .service__icon { width: 44px; height: 44px; flex: none; }
</style>
</head>
<body>

<section class="card card--front" aria-label="Business card front">
  <svg class="card__lines" viewBox="0 0 700 400" aria-hidden="true">
    <line x1="50" y1="160" x2="390" y2="160" stroke="#f2f2f2" stroke-width="1.5"/>
    <circle cx="396" cy="160" r="6" fill="none" stroke="#f2f2f2" stroke-width="2"/>
    <circle cx="420" cy="270" r="6" fill="none" stroke="#e8202a" stroke-width="2"/>
    <line x1="426" y1="270" x2="670" y2="270" stroke="#e8202a" stroke-width="1.5"/>
  </svg>

  <div class="brand-name">TQ Networks</div>

  <div class="holder">
    <div class="holder__name">Dwayne Falstrup</div>
    <div class="holder__title">Director</div>
  </div>

  <ul class="contacts">
    <li>03 6193 4827
      <svg viewBox="0 0 16 16"><path d="M3 1l3 3-2 2c1 2 3 4 5 5l2-2 3 3-2 3C6 15 1 10 1 3z" fill="#e8202a"/></svg></li>
    <li>0412 587 239
      <svg viewBox="0 0 16 16"><rect x="4" y="1" width="8" height="14" rx="1.5" fill="none" stroke="#e8202a" stroke-width="1.6"/><circle cx="8" cy="12.5" r="1" fill="#e8202a"/></svg></li>
    <li>dwayne@tqnetworks.com.au
      <svg viewBox="0 0 16 16"><rect x="1" y="3" width="14" height="10" fill="#e8202a"/><path d="M1 3l7 6 7-6" fill="none" stroke="#141414" stroke-width="1.4"/></svg></li>
    <li>www.tqnetworks.com.au
      <svg viewBox="0 0 16 16"><circle cx="8" cy="8" r="6.5" fill="none" stroke="#e8202a" stroke-width="1.4"/><ellipse cx="8" cy="8" rx="3" ry="6.5" fill="none" stroke="#e8202a" stroke-width="1.2"/><line x1="1.5" y1="8" x2="14.5" y2="8" stroke="#e8202a" stroke-width="1.2"/></svg></li>
  </ul>
</section>

<section class="card card--back" aria-label="Business card back">
  <svg class="card__lines" viewBox="0 0 700 400" aria-hidden="true" fill="none" stroke="#e8202a" stroke-width="1.3">
    <polyline points="60,96 70,110 420,110"/><circle cx="426" cy="110" r="5" stroke-width="2"/>
    <polyline points="60,152 70,166 400,166"/><circle cx="406" cy="166" r="5" stroke-width="2"/>
    <polyline points="60,208 70,222 380,222"/><circle cx="386" cy="222" r="5" stroke-width="2"/>
    <polyline points="60,264 70,278 360,278"/><circle cx="366" cy="278" r="5" stroke-width="2"/>
    <polyline points="60,320 70,334 340,334"/><circle cx="346" cy="334" r="5" stroke-width="2"/>
  </svg>

  <ul class="services">
    <li class="service">
      <svg class="service__icon" viewBox="0 0 44 44"><circle cx="22" cy="22" r="20" fill="#141414" stroke="#e8202a" stroke-width="2.5"/><circle cx="18" cy="17" r="4" fill="#e8202a"/><path d="M10 30c0-5 4-8 8-8s8 3 8 8z" fill="#e8202a"/><circle cx="30" cy="24" r="3.5" fill="none" stroke="#e8202a" stroke-width="2.5" stroke-dasharray="2 1.5"/></svg>
      Managed IT Services</li>
    <li class="service">
      <svg class="service__icon" viewBox="0 0 44 44"><circle cx="22" cy="22" r="20" fill="#141414" stroke="#e8202a" stroke-width="2.5"/><rect x="12" y="25" width="4" height="6" fill="#e8202a"/><rect x="19" y="21" width="4" height="10" fill="#e8202a"/><rect x="26" y="16" width="4" height="15" fill="#e8202a"/><path d="M11 20l9-6 4 3 8-5" stroke="#e8202a" stroke-width="1.8" fill="none"/></svg>
      Productivity Solutions</li>
    <li class="service">
      <svg class="service__icon" viewBox="0 0 44 44"><circle cx="22" cy="22" r="20" fill="#141414" stroke="#e8202a" stroke-width="2.5"/><ellipse cx="20" cy="14" rx="8" ry="3" fill="#e8202a"/><path d="M12 15v12c0 2 4 3 8 3s8-1 8-3V15c0 2-4 3-8 3s-8-1-8-3z" fill="#e8202a"/><circle cx="29" cy="27" r="5" fill="#141414" stroke="#e8202a" stroke-width="2"/></svg>
      Data Backup and Recovery</li>
    <li class="service">
      <svg class="service__icon" viewBox="0 0 44 44"><circle cx="22" cy="22" r="20" fill="#141414" stroke="#e8202a" stroke-width="2.5"/><circle cx="22" cy="22" r="8" fill="none" stroke="#e8202a" stroke-width="4" stroke-dasharray="3 2.3"/><circle cx="22" cy="22" r="3" fill="#e8202a"/></svg>
      IT System Maintenance</li>
    <li class="service">
      <svg class="service__icon" viewBox="0 0 44 44"><circle cx="22" cy="22" r="20" fill="#141414" stroke="#e8202a" stroke-width="2.5"/><path d="M22 10l9 3v7c0 6-4 10-9 12-5-2-9-6-9-12v-7z" fill="none" stroke="#e8202a" stroke-width="2"/><rect x="18" y="20" width="8" height="6" fill="#e8202a"/><path d="M19.5 20v-2a2.5 2.5 0 0 1 5 0v2" fill="none" stroke="#e8202a" stroke-width="1.6"/></svg>
      Managed IT Security</li>
  </ul>

  <div class="brand-name">TQ Networks</div>
</section>

</body>
</html>
```